Seventy Crumbs needs a business card

Seventy Crumbs needs an attractive, playful, and exciting business card design to attract potential buyers. I have included our logo, label, and social media design files along with the fonts and colors for ideas. For the logo file, please only pay attention to the purple background with white text. I want a card with premium matte and metallic finish. I want my name included, e-mail, and phone number. The logo must be included, and then use the label design and social media design files to add creativity to the design. Only the fonts that are provided should be used as well.

Name: Gregory Talliston
Phone: 555-417-2086
E-mail: gtalliston@seventycrumbs.example

Contact Information for Business Card

I want a card with premium matte and metallic finish. I want my name included, e-mail, and phone number. The logo must be included, and then use the label design and social media design files to add creativity to the design. Only the fonts that are provided should be used as well.

Name: Gregory Talliston
Phone: 555-417-2086

Colors
6b449b

Requirements
Must have
• My logo, my fonts, my colors, my designs to some degree, and my character

```html
<!DOCTYPE html>
<html lang="en">
<head>
<meta charset="utf-8">
<title>Seventy Crumbs – Business Card</title>
<link href="https://fonts.googleapis.com/css2?family=Roboto+Condensed:wght@400;700&family=Roboto:wght@400&family=Handlee&display=swap" rel="stylesheet">
<style>
  :root {
    --backdrop: #2b2b2b;
    --card-purple: #361d60;
    --gold: #d6ad63;
    --gold-light: #e7c98a;
    --white: #ffffff;
  }
  html, body {
    margin: 0;
    padding: 0;
    width: 1200px;
    height: 960px;
    overflow: hidden;
    background: var(--backdrop);
  }
  .canvas {
    position: relative;
    width: 1200px;
    height: 960px;
  }
  .card {
    position: absolute;
    left: 320px;
    width: 600px;
    background: var(--card-purple);
    box-sizing: border-box;
  }
  .card-back {
    top: 104px;
    height: 344px;
  }
  .card-front {
    top: 493px;
    height: 343px;
    overflow: hidden;
  }
  .brand-name {
    position: absolute;
    margin: 0;
    color: var(--gold);
    font-family: "Roboto Condensed", sans-serif;
    font-weight: 700;
    text-align: center;
    white-space: nowrap;
  }
  .card-back .brand-name {
    left: 0;
    right: 0;
    top: 150px;
    font-size: 44px;
  }
  .card-front .brand-name {
    left: 400px;
    width: 180px;
    top: 100px;
    font-size: 30px;
    line-height: 1.1;
    white-space: normal;
  }
  .back-website {
    position: absolute;
    left: 0;
    right: 0;
    top: 290px;
    margin: 0;
    text-align: center;
    color: var(--gold);
    font-family: "Handlee", cursive;
    font-size: 19px;
  }
  .holder-name {
    position: absolute;
    left: 31px;
    top: 192px;
    margin: 0;
    color: var(--gold);
    font-family: "Roboto Condensed", sans-serif;
    font-weight: 700;
    font-size: 23px;
    letter-spacing: 0.2px;
  }
  .name-rule {
    position: absolute;
    left: 31px;
    top: 227px;
    width: 531px;
    height: 2px;
    background: var(--white);
  }
  .contact-list {
    position: absolute;
    left: 32px;
    top: 244px;
    margin: 0;
    padding: 0;
    list-style: none;
    color: var(--white);
    font-family: "Roboto", sans-serif;
    font-size: 14px;
  }
  .contact-list li {
    display: flex;
    align-items: center;
    height: 19.5px;
  }
  .contact-list svg {
    width: 12px;
    height: 12px;
    margin-right: 10px;
    fill: var(--gold-light);
  }
  .edge-rule {
    position: absolute;
    left: 0;
    right: 0;
    top: 321px;
    height: 2px;
    background: var(--white);
  }
  .edge-band {
    position: absolute;
    left: 0;
    right: 0;
    top: 324px;
    height: 19px;
    background: linear-gradient(180deg, var(--gold-light), var(--gold));
  }
</style>
</head>
<body>
<main class="canvas">
  <section class="card card-back" aria-label="Card back">
    <p class="brand-name">Seventy Crumbs</p>
    <p class="back-website">www.seventycrumbs.example</p>
  </section>

  <section class="card card-front" aria-label="Card front">
    <p class="brand-name">Seventy Crumbs</p>
    <h1 class="holder-name">GREGORY TALLISTON</h1>
    <div class="name-rule"></div>
    <ul class="contact-list">
      <li>
        <svg viewBox="0 0 24 24" aria-hidden="true"><path d="M6.6 10.8a15.1 15.1 0 0 0 6.6 6.6l2.2-2.2c.3-.3.7-.4 1-.2 1.1.4 2.3.6 3.6.6.6 0 1 .4 1 1V20c0 .6-.4 1-1 1A17 17 0 0 1 3 4c0-.6.4-1 1-1h3.5c.6 0 1 .4 1 1 0 1.3.2 2.5.6 3.6.1.3 0 .7-.2 1z"/></svg>
        555-417-2086
      </li>
      <li>
        <svg viewBox="0 0 24 24" aria-hidden="true"><path d="M2 5h20v14H2z M2 5l10 8 10-8" /><path d="M3 6l9 7 9-7" fill="#361d60"/></svg>
        gtalliston@seventycrumbs.example
      </li>
      <li>
        <svg viewBox="0 0 24 24" aria-hidden="true"><circle cx="12" cy="12" r="10"/><path d="M7 7c2 1 3 3 2 5s1 4 3 5M14 4c-1 2 0 3 2 4s3 3 2 5" stroke="#361d60" stroke-width="1.6" fill="none"/></svg>
        www.seventycrumbs.example
      </li>
    </ul>
    <div class="edge-rule"></div>
    <div class="edge-band"></div>
  </section>
</main>
</body>
</html>
```